Corwell Facilities Services Business Card.

We need a card for Corwell Facilities Services with a new look. We also have service and supply partners that we would like to have on the card. Lumacoat is a surface application company, Corwell Facilities is a facilities services business, Tavish Supply Co is a Facilities supply business, Pelvra is a product that we use that powers our business.

```html
<!DOCTYPE html>
<html lang="en">
<head>
<meta charset="utf-8">
<title>Corwell Facilities Services – Business Card</title>
<link rel="stylesheet" href="https://fonts.googleapis.com/css2?family=Roboto:ital,wght@0,400;0,500;0,700;1,400&display=swap">
<style>
  :root {
    --brand-blue: #1a78c2;
    --brand-green: #3bb44a;
    --deep-green: #1d6e2b;
    --ink: #1b1b1b;
    --navy: #12305a;
    --band-grey: #d1d2d4;
    --photo-dark: #5a5a5a;
    --photo-light: #b5b5b5;
    --frame: #555;
  }
  * { box-sizing: border-box; margin: 0; padding: 0; }
  html, body { width: 1200px; height: 1200px; overflow: hidden; background: #fff; }
  body { position: relative; font-family: "Roboto", Arial, sans-serif; color: var(--ink); }

  .card {
    position: absolute; left: 185px; width: 842px; height: 482px;
    border: 1px solid var(--frame); background: #fff; overflow: hidden;
  }
  .card--front { top: 90px; }
  .card--back { top: 629px; }

  /* Front */
  .brand-mark { position: absolute; left: 58px; top: 58px; display: flex; align-items: center; gap: 12px; }
  .brand-mark__dot { width: 34px; height: 34px; border-radius: 50%; background: var(--brand-green); }
  .brand-mark__name { font-weight: 700; font-size: 30px; line-height: 1.1; color: var(--brand-blue); width: 260px; }

  .holder { position: absolute; left: 147px; top: 200px; }
  .holder__name { font-weight: 700; font-size: 40px; color: var(--brand-green); letter-spacing: 0.5px; }
  .holder__title { font-size: 26px; color: var(--brand-blue); margin-top: 2px; }

  .details { position: absolute; left: 534px; top: 52px; }
  .details__company { font-size: 24px; color: var(--brand-blue); }
  .details__address { font-size: 19px; line-height: 24px; margin-top: 2px; }

  .contacts { position: absolute; left: 534px; top: 200px; list-style: none; }
  .contacts li { display: flex; align-items: center; height: 34px; font-size: 19px; }
  .contacts svg { width: 30px; height: 26px; margin-right: 8px; flex: none; }

  .tagline-band {
    position: absolute; left: 0; bottom: 0; width: 100%; height: 113px;
    background: var(--band-grey); display: flex; align-items: center; justify-content: center;
    text-align: center; font-style: italic; font-size: 27px; line-height: 32px; color: var(--brand-blue);
  }

  /* Back */
  .hero { position: absolute; left: 0; top: 0; width: 842px; height: 332px; }
  .partners { position: absolute; left: 0; top: 332px; width: 100%; height: 150px; }
  .partner { position: absolute; top: 0; height: 150px; display: flex; flex-direction: column; justify-content: center; }
  .partner--pelvra { left: 76px; }
  .partner__lead { font-size: 19px; color: var(--navy); }
  .partner__name { font-weight: 700; font-size: 38px; color: var(--navy); letter-spacing: 1px; }
  .partner--lumacoat { left: 300px; width: 215px; align-items: center; }
  .partner--lumacoat .partner__name { color: var(--brand-blue); font-size: 32px; }
  .partner--tavish { left: 572px; flex-direction: row; align-items: center; gap: 12px; }
  .partner__square { width: 46px; height: 46px; background: #5b8fd6; }
  .partner--tavish .partner__name { color: #5b8fd6; font-size: 26px; letter-spacing: 0; }
</style>
</head>
<body>

<section class="card card--front">
  <div class="brand-mark">
    <span class="brand-mark__dot"></span>
    <span class="brand-mark__name">Corwell Facilities Services</span>
  </div>

  <div class="holder">
    <h1 class="holder__name">Daniel Reyes</h1>
    <p class="holder__title">Manager</p>
  </div>

  <div class="details">
    <p class="details__company">Corwell Facilities Services</p>
    <p class="details__address">Dummy Address<br>Lorem Ipsum<br>Sit Amet<br>Lorem Ipsum</p>
  </div>

  <ul class="contacts">
    <li>
      <svg viewBox="0 0 30 26"><path d="M6 3 l5 0 l2 6 l-3 2 q2 5 7 8 l2 -3 l6 2 l0 5 q-14 1 -19 -20z" fill="var(--brand-green)"/></svg>
      1-800-555-0142
    </li>
    <li>
      <svg viewBox="0 0 30 26"><rect x="3" y="1" width="14" height="24" rx="2" fill="none" stroke="var(--brand-green)" stroke-width="2.4"/><circle cx="10" cy="21" r="1.4" fill="var(--brand-green)"/></svg>
      07700 900123
    </li>
    <li>
      <svg viewBox="0 0 30 26"><rect x="2" y="5" width="26" height="16" fill="none" stroke="var(--brand-green)" stroke-width="2.4"/><path d="M2 5 l13 10 l13 -10" fill="none" stroke="var(--brand-green)" stroke-width="2.4"/></svg>
      danielreyes@example.com
    </li>
    <li>
      <svg viewBox="0 0 30 26"><g fill="none" stroke="var(--brand-green)" stroke-width="2"><circle cx="14" cy="13" r="11"/><ellipse cx="14" cy="13" rx="5" ry="11"/><path d="M3 13h22M5 7h18M5 19h18"/></g></svg>
      www.corwellfacilities.com
    </li>
  </ul>

  <div class="tagline-band">
    <p>Providing high-quality facilities service<br>solutions to the industries we serve.</p>
  </div>
</section>

<section class="card card--back">
  <svg class="hero" viewBox="0 0 842 332" preserveAspectRatio="none">
    <defs>
      <linearGradient id="floorShade" x1="0" y1="0" x2="0" y2="1">
        <stop offset="0" stop-color="var(--photo-dark)"/>
        <stop offset="0.72" stop-color="#6d6d6d"/>
        <stop offset="0.76" stop-color="var(--photo-light)"/>
        <stop offset="1" stop-color="#9a9a9a"/>
      </linearGradient>
    </defs>
    <rect width="842" height="332" fill="url(#floorShade)" role="img" aria-label="Photo of a cleaner mopping a polished floor beside a grey wall"/>
    <path d="M0,14 C250,30 420,120 500,200 C600,290 720,312 842,316 L842,332 L0,332 Z" fill="var(--deep-green)" opacity="0.88"/>
  </svg>

  <div class="partners">
    <div class="partner partner--pelvra">
      <span class="partner__lead">Powered by</span>
      <span class="partner__name">PELVRA</span>
    </div>
    <div class="partner partner--lumacoat">
      <span class="partner__name">LUMACOAT</span>
    </div>
    <div class="partner partner--tavish">
      <span class="partner__square"></span>
      <span class="partner__name">Tavish Supply Co</span>
    </div>
  </div>
</section>

</body>
</html>
```